International aerospace industry business needs a new brochure

We need to make a new Brochure 4 pages A4:
- like the old one (file Veknorame_test_coupons_thermal_spray.pdf)
- with the new text (tekst_na_ulotke_v9.docx)
- with the new design as in email graphic (20201019_FINAL_Test Coupons v2.psd or .png).

Requirements
Must have
• design as in email graphic (20201019_FINAL_Test Coupons v2.psd or .png)
with the new text (tekst_na_ulotke_v9.docx)
Nice to have
• photos with our employees on production floor may be used.

```html
<!DOCTYPE html>
<html lang="en">
<head>
<meta charset="utf-8">
<title>Veknorame – Test Specimens Brochure</title>
<link rel="stylesheet" href="https://fonts.googleapis.com/css2?family=Noto+Sans:wght@400;700;800&family=Source+Sans+3:wght@400&display=swap">
<style>
  :root {
    --orange: #f39314;
    --navy: #24418f;
    --blue: #2e4fa0;
    --grey-icon: #8a8a8a;
    --rule: #dcdcdc;
    --ink: #1a1a1a;
    --backdrop: #e6e6e6;
    --paper: #ffffff;
    --deco-grey: #dedede;
  }
  * { box-sizing: border-box; margin: 0; padding: 0; }
  html, body { width: 1080px; height: 1200px; overflow: hidden; }
  body { background: var(--backdrop); font-family: "Noto Sans", sans-serif; color: var(--ink); }

  .page { position: absolute; left: 116px; top: 0; width: 848px; height: 1200px; background: var(--paper); overflow: hidden; }

  .deco { position: absolute; inset: 0; width: 848px; height: 1200px; }

  .section-title { position: absolute; left: 50px; color: var(--orange); font-weight: 800; font-size: 31px; line-height: 32px; letter-spacing: 0.3px; }
  .citation-title { top: 46px; }
  .advantages-title { top: 266px; }
  .experience-title { top: 712px; left: 53px; }

  .citation-text { position: absolute; left: 53px; top: 97px; width: 240px; font-size: 14px; line-height: 17px; }

  .coupons-photo { position: absolute; left: 326px; top: 32px; width: 522px; height: 204px; }

  .divider { position: absolute; top: 323px; width: 1px; height: 285px; background: var(--rule); }
  .advantage-rule { position: absolute; top: 419px; height: 2px; background: var(--rule); }

  .advantage { position: absolute; top: 421px; width: 212px; }
  .advantage::before { content: ""; position: absolute; left: 0; top: 0; right: 0; height: 110px; background: linear-gradient(#eef0f4, rgba(255,255,255,0)); }
  .advantage h3 { position: relative; color: var(--navy); font-weight: 800; font-size: 20.5px; line-height: 24px; padding: 10px 0 0 12px; }
  .advantage p { position: relative; font-size: 14px; line-height: 17px; padding: 17px 0 0 12px; }
  .icon { position: absolute; top: 333px; }

  .intro { position: absolute; left: 53px; top: 637px; width: 745px; font-size: 14.4px; line-height: 17px; }

  .specimen-card { position: absolute; top: 804px; width: 238px; height: 361px; border-top: 2px solid var(--orange); border-left: 2px solid var(--orange); border-right: 9px solid var(--orange); border-bottom: 9px solid var(--orange); background: var(--paper); padding: 4px 14px 4px 12px; display: flex; flex-direction: column; }
  .specimen-row { flex: 1; display: flex; align-items: center; justify-content: space-between; border-bottom: 1px solid var(--rule); font-family: "Source Sans 3", sans-serif; font-size: 12px; line-height: 14px; }
  .specimen-row:last-child { border-bottom: none; }
  .specimen-row span { width: 100px; }
  .specimen-shape { background: linear-gradient(180deg, #c9ccd0, #7f8489); border-radius: 3px; }
  .disc { width: 72px; height: 30px; border-radius: 50% / 40%; }
  .bar { width: 76px; height: 10px; }
  .plate { width: 82px; height: 16px; }
  .tube { width: 36px; height: 44px; border-radius: 4px; }
  .strip { width: 100px; height: 7px; }
</style>
</head>
<body>
<main class="page">
  <svg class="deco" viewBox="0 0 848 1200" aria-hidden="true">
    <polygon points="0,819 0,1200 218,1200" fill="var(--deco-grey)"/>
    <polygon points="848,1121 848,1200 802,1200" fill="var(--orange)"/>
  </svg>

  <h1 class="section-title citation-title">Citation</h1>
  <p class="citation-text">“A test coupon or simply a coupon is a small sample of the material used to obtain data of specific properties after the testing. More often it is called a specimen or just a sample.”</p>

  <svg class="coupons-photo" viewBox="0 0 522 204">
    <defs>
      <linearGradient id="metal" x1="0" y1="0" x2="1" y2="1">
        <stop offset="0" stop-color="#e4e6e3"/>
        <stop offset="1" stop-color="#a9aeab"/>
      </linearGradient>
    </defs>
    <polygon points="118,0 522,0 522,204 0,204" fill="url(#metal)" role="img" aria-label="Pile of round and square machined metal test coupons"/>
    <polygon points="522,59 522,204 437,204" fill="var(--navy)"/>
    <polygon points="118,0 522,0 522,3 116,3" fill="var(--orange)"/>
    <polygon points="2,201 522,201 522,204 0,204" fill="var(--orange)"/>
  </svg>

  <h2 class="section-title advantages-title">Our Advantages</h2>

  <div class="divider" style="left:283px"></div>
  <div class="divider" style="left:566px"></div>
  <div class="advantage-rule" style="left:0;width:256px"></div>
  <div class="advantage-rule" style="left:308px;width:232px"></div>
  <div class="advantage-rule" style="left:594px;width:254px"></div>

  <svg class="icon" style="left:67px" width="56" height="78" viewBox="0 0 56 78" aria-hidden="true">
    <polygon points="18,44 8,68 16,66 21,74 28,52" fill="var(--grey-icon)"/>
    <polygon points="38,44 48,68 40,66 35,74 28,52" fill="var(--grey-icon)"/>
    <circle cx="28" cy="26" r="22" fill="var(--blue)" stroke="var(--blue)" stroke-width="6" stroke-dasharray="5 4"/>
    <circle cx="28" cy="26" r="11" fill="#fff"/>
  </svg>

  <svg class="icon" style="left:378px" width="94" height="80" viewBox="0 0 94 80" aria-hidden="true">
    <circle cx="30" cy="52" r="21" fill="none" stroke="var(--blue)" stroke-width="10" stroke-dasharray="6 5"/>
    <circle cx="30" cy="52" r="15" fill="none" stroke="var(--blue)" stroke-width="8"/>
    <circle cx="72" cy="37" r="13" fill="none" stroke="var(--grey-icon)" stroke-width="7" stroke-dasharray="4 3"/>
    <circle cx="72" cy="37" r="9" fill="none" stroke="var(--grey-icon)" stroke-width="5"/>
    <circle cx="55" cy="12" r="9" fill="none" stroke="var(--grey-icon)" stroke-width="5" stroke-dasharray="3 2.5"/>
    <circle cx="55" cy="12" r="6" fill="none" stroke="var(--grey-icon)" stroke-width="4"/>
  </svg>

  <svg class="icon" style="left:616px;top:350px" width="94" height="56" viewBox="0 0 94 56" aria-hidden="true">
    <rect x="30" y="0" width="64" height="34" fill="var(--blue)"/>
    <path d="M0 42 V26 L10 12 H28 V42 Z" fill="var(--grey-icon)"/>
    <path d="M5 24 L12 15 H22 V24 Z" fill="#fff"/>
    <rect x="0" y="36" width="94" height="8" fill="var(--grey-icon)"/>
    <g fill="#fff" stroke="var(--grey-icon)" stroke-width="4">
      <circle cx="14" cy="46" r="6"/><circle cx="60" cy="46" r="6"/><circle cx="78" cy="46" r="6"/>
    </g>
  </svg>

  <section class="advantage" style="left:45px">
    <h3>Quality<br>Assurance</h3>
    <p>We maintain Quality Management System in accordance with ISO 9001: 2015 and AS 9100D: 2016 by qualified staff of internal auditors.</p>
  </section>
  <section class="advantage" style="left:318px">
    <h3>Manufacturing<br>processes</h3>
    <p>Using modern machining, loss and additive methods we ensure optimum price / performance ratio while meeting all requirements of the project.</p>
  </section>
  <section class="advantage" style="left:606px">
    <h3>In-time<br>Delivery</h3>
    <p>Reliable processing from the design phase to the delivery to Customer through the Just-in-Time method.</p>
  </section>

  <p class="intro">spec.samples is a product line of specimens, samples and coupons machined from difficult-to-machine aerospace grade materials such as nickel &amp; cobalt base superalloys, titanium, and hardened steel. The brand is based on experience and know-how of Veknorame company.</p>

  <h2 class="section-title experience-title">Our experience includes<br>manufacturing the specimens:</h2>

  <div class="specimen-card" style="left:53px">
    <div class="specimen-row"><span>Adhesion, cohesion &amp; bond strength test of coating</span><div class="specimen-shape disc" role="img" aria-label="Coating bond test disc"></div></div>
    <div class="specimen-row"><span>Fatigue specimen blended</span><div class="specimen-shape bar" role="img" aria-label="Blended fatigue specimen"></div></div>
    <div class="specimen-row"><span>Fatigue specimen</span><div class="specimen-shape bar" role="img" aria-label="Fatigue specimen"></div></div>
    <div class="specimen-row"><span>FCT test</span><div class="specimen-shape disc" style="height:24px;width:80px" role="img" aria-label="FCT test disc"></div></div>
    <div class="specimen-row"><span>Stress corosion</span><div class="specimen-shape tube" role="img" aria-label="Stress corrosion specimen"></div></div>
    <div class="specimen-row"><span>Tensile test</span><div class="specimen-shape strip" role="img" aria-label="Tensile test strip"></div></div>
  </div>

  <div class="specimen-card" style="left:303px">
    <div class="specimen-row"><span>Test panel erosion test</span><div class="specimen-shape plate" style="height:26px;width:76px" role="img" aria-label="Erosion test panel"></div></div>
    <div class="specimen-row"><span>Test panel for bend</span><div class="specimen-shape plate" style="height:12px;width:96px" role="img" aria-label="Bend test panel"></div></div>
    <div class="specimen-row"><span>Test panel for Hoffman scratch test</span><div class="specimen-shape plate" style="height:20px;width:90px" role="img" aria-label="Scratch test panel"></div></div>
    <div class="specimen-row"><span>Test panel for microstructure evaluation</span><div class="specimen-shape plate" style="height:12px;width:108px" role="img" aria-label="Microstructure test panel"></div></div>
    <div class="specimen-row"><span>Test panel for shear triple-lug shear test</span><div class="specimen-shape plate" style="height:24px;width:102px" role="img" aria-label="Shear test panel"></div></div>
    <div class="specimen-row"><span>Test panel hardness test</span><div class="specimen-shape plate" style="height:32px;width:86px" role="img" aria-label="Hardness test panel"></div></div>
  </div>

  <div class="specimen-card" style="left:553px">
    <div class="specimen-row"><span>Adhesion, cohesion &amp; bond strength test of coating</span><div class="specimen-shape disc" role="img" aria-label="Coating bond test disc"></div></div>
    <div class="specimen-row"><span>Fatigue specimen blended</span><div class="specimen-shape bar" role="img" aria-label="Blended fatigue specimen"></div></div>
    <div class="specimen-row"><span>Fatigue specimen</span><div class="specimen-shape bar" role="img" aria-label="Fatigue specimen"></div></div>
    <div class="specimen-row"><span>FCT test</span><div class="specimen-shape disc" style="height:24px;width:80px" role="img" aria-label="FCT test disc"></div></div>
    <div class="specimen-row"><span>Stress corosion</span><div class="specimen-shape tube" role="img" aria-label="Stress corrosion specimen"></div></div>
    <div class="specimen-row"><span>Tensile test</span><div class="specimen-shape strip" role="img" aria-label="Tensile test strip"></div></div>
  </div>
</main>
</body>
</html>
```